Design for a very long wall that will be wall printed. The name of the facility is "Brisk Gallery"

The space I am working on has a 30' x 8' wall. It is a wall that is located in a under construction Design Showroom where contractors of all trades can have an office and put out their banners and different items for customers to come and see. so there could be roofers, construction, cabinet installers and designers, gutters and other trades can rent an office in the space and bring their customers and sit down and talk about what they need. I want the design for the wall to have a bold punch and it will be printed on the wall with a high definition wall printer. The walls are arctic white right now and I can send the color codes for the color the wall is currently. The wall printer has the capability to do white as well. I am including some pics of the space and an example wall print.

Target Market(s)

Contractors and Customers of Contractors

Industry/Entity Type

all trades. Photos are to demonstrate the capabilities of the printer that will be used

Requirements
Must have
• Perhaps have a person or persons int he design, a human element and perhaps some abstract elements as well
Nice to have
• Perhaps some architecture or perhaps an interior cabinet or fixtures. Glass doors and or walls. Perhaps incorporate the name "Brisk Gallery"

```html
<!DOCTYPE html>
<html lang="en">
<head>
<meta charset="utf-8">
<title>Feel the Rhythm of Abstract Creativity</title>
<link rel="stylesheet" href="https://fonts.googleapis.com/css2?family=Source+Sans+3:wght@300;700&display=swap">
<style>
  :root {
    --wall-light: #f8f8f8;
    --wall-shade: #e6e6e7;
    --sun-yellow: #fdc32b;
    --coral-red: #ef4541;
    --teal: #0b97b4;
    --ink: #4a4d57;
    --mist: #d6d6d8;
    --stone-pale: #ececee;
    --stone-light: #d7d8dc;
    --stone-mid: #a9abb3;
    --stone-deep: #8a8c96;
  }
  html, body {
    margin: 0;
    padding: 0;
    overflow: hidden;
  }
  .wall-mural {
    position: relative;
    width: 1200px;
    height: 320px;
    overflow: hidden;
    background: linear-gradient(90deg, var(--wall-light) 0%, var(--wall-light) 55%, var(--wall-shade) 100%);
    font-family: "Source Sans 3", sans-serif;
  }
  .mural-art {
    position: absolute;
    inset: 0;
    width: 1200px;
    height: 320px;
  }
  .headline {
    position: absolute;
    left: 857px;
    top: 147px;
    margin: 0;
    color: var(--ink);
    line-height: 1;
    font-weight: normal;
  }
  .headline-light {
    display: block;
    margin-left: 8px;
    font-weight: 300;
    font-size: 28px;
    letter-spacing: -0.4px;
  }
  .headline-bold {
    display: block;
    margin-top: -1px;
    font-weight: 700;
    font-size: 29px;
    letter-spacing: -0.9px;
  }
</style>
</head>
<body>
<main class="wall-mural">
  <svg class="mural-art" viewBox="0 0 1200 320" xmlns="http://www.w3.org/2000/svg">
    <defs>
      <radialGradient id="bust-tone" cx="0.62" cy="0.5" r="0.75">
        <stop offset="0" stop-color="var(--stone-mid)"/>
        <stop offset="0.45" stop-color="var(--stone-light)"/>
        <stop offset="1" stop-color="var(--stone-pale)"/>
      </radialGradient>
      <linearGradient id="foliage-tone" x1="0" y1="0" x2="1" y2="0">
        <stop offset="0" stop-color="var(--stone-light)" stop-opacity="0"/>
        <stop offset="1" stop-color="var(--stone-deep)" stop-opacity="0.55"/>
      </linearGradient>
      <linearGradient id="mesh-tone" x1="0" y1="0" x2="1" y2="0">
        <stop offset="0" stop-color="#ececee"/>
        <stop offset="1" stop-color="#b4b6bc"/>
      </linearGradient>
    </defs>

    <!-- hero sun disc -->
    <circle class="sun-disc" cx="244.5" cy="179.3" r="137.4" fill="var(--sun-yellow)"/>

    <!-- classical bust illustration area -->
    <g class="bust-illustration" role="img" aria-label="Engraved classical bust of a bearded man crowned with vines, leaves and fruit">
      <path d="M0,40 C20,28 60,30 90,22 C130,10 170,20 200,10 C230,2 260,12 290,30
               C318,46 330,80 326,120 C322,160 340,200 318,240 C300,272 270,300 232,320
               H0 Z" fill="url(#bust-tone)"/>
      <path d="M240,40 C290,38 330,80 326,130 C322,180 338,220 312,252 C292,276 262,300 232,320
               H200 C240,280 262,220 260,160 C258,110 250,70 240,40 Z" fill="url(#foliage-tone)"/>
    </g>

    <!-- wireframe head dome -->
    <path class="mesh-head" role="img" aria-label="Wireframe mesh of a human head in profile"
          d="M461.3,187.7 A120,120 0 0 1 701.3,187.7 Z" fill="url(#mesh-tone)" opacity="0.85"/>

    <circle class="red-orb" cx="548.7" cy="166.8" r="50.3" fill="var(--coral-red)" opacity="0.92"/>
    <circle class="accent-dot" cx="670.8" cy="157.4" r="11" fill="var(--sun-yellow)"/>

    <!-- lower half sun -->
    <path class="half-sun" d="M597.7,187.7 A87,87 0 0 0 771.7,187.7 Z" fill="var(--sun-yellow)"/>

    <!-- horizon line -->
    <line class="horizon" x1="340" y1="187.7" x2="844.5" y2="187.7" stroke="var(--ink)" stroke-width="0.9"/>

    <!-- scattered orbs -->
    <circle cx="799.8" cy="203.1" r="24" fill="var(--teal)"/>
    <circle cx="396.4" cy="117.8" r="9.3" fill="var(--teal)"/>
    <circle cx="433.2" cy="238.5" r="16.3" fill="var(--sun-yellow)"/>
    <circle cx="464.9" cy="188.2" r="6.5" fill="var(--sun-yellow)"/>
    <circle cx="590.2" cy="236.6" r="8" fill="var(--sun-yellow)"/>
    <circle cx="422.5" cy="283.7" r="7" fill="var(--sun-yellow)"/>
    <circle cx="363.3" cy="284.6" r="3.7" fill="var(--sun-yellow)"/>
    <circle cx="750" cy="86" r="9" fill="var(--sun-yellow)"/>
    <circle cx="852" cy="76.4" r="13.5" fill="var(--coral-red)"/>
    <circle cx="830.5" cy="135.5" r="10" fill="var(--mist)"/>
    <circle cx="852" cy="14" r="3.3" fill="var(--sun-yellow)"/>
    <circle cx="839" cy="53" r="3.3" fill="var(--sun-yellow)"/>
    <circle cx="822" cy="58" r="2.3" fill="var(--sun-yellow)"/>
    <circle cx="811" cy="38.7" r="1.3" fill="var(--sun-yellow)"/>
    <circle cx="866" cy="131" r="1.4" fill="var(--sun-yellow)"/>
  </svg>

  <h1 class="headline">
    <span class="headline-light">Feel the Rhythm of</span>
    <span class="headline-bold">Abstract Creativity</span>
  </h1>
</main>
</body>
</html>
```